Owen Tasker Studios Business Card

Looking for a clear, modern, elegant, sharp business card that conveys a professional yet edgy image to my business as a wedding, portrait, and travel photographer. Would like something that looks vintage yet modern. Need a new business card to grow my business. We are growing the business for Wedding and Event Photography as well as fine art Photography. (Mostly Landscapes)
Updates

I’m looking through designs now but I have a new logo that i want using please.

New logo uploaded please redesign using that

PLEASE ALL DESIGNERS LOOK IN BRIEF FOR NEW LOGO

Target Market(s)

Brides, Grooms, Families with Kids, People looking for Fine Art Photography Artwork

Industry/Entity Type

Photographer

Contact Information for Business Card

Unsure

Font styles to use
Serif

Colors

Designer to choose colors to be used in the design.

Requirements
Must have
• My Website:
• http://taskerlens.examplefolio.net
• Phone:
• 323-481-5206
• Email:
• owentaskerlens@mailbox-example.net
Nice to have
• Would like a sort of shine on the printing finish.
• I like black I think it looks good on a business card.
• Can try working with my logo (png that I've attached)

```html
<!DOCTYPE html>
<html lang="en">
<head>
<meta charset="utf-8">
<title>Owen Tasker Studios Business Card</title>
<link rel="stylesheet" href="https://fonts.googleapis.com/css2?family=Lato:wght@300;400&display=swap">
<style>
  :root {
    --backdrop: #5c5c5c;
    --card: #1d1d1e;
    --card-edge: #161617;
    --gloss-deep: #0b0b0c;
    --gloss-sheen: #9a9a9c;
    --ink: #e9e9e9;
    --ink-soft: #bdbdbd;
  }
  * { margin: 0; padding: 0; box-sizing: border-box; }
  html, body { width: 801px; height: 1200px; overflow: hidden; }
  body {
    background: var(--backdrop);
    font-family: "Lato", "Helvetica Neue", Arial, sans-serif;
    color: var(--ink);
    position: relative;
  }
  .card {
    position: absolute;
    left: 90px;
    width: 620px;
    height: 354px;
    background: var(--card);
    border: 1px solid var(--card-edge);
    box-shadow: 0 10px 28px rgba(0,0,0,0.35);
    overflow: hidden;
  }
  .card--front { top: 110px; }
  .card--back { top: 700px; }

  /* front: glossy spot-varnish area */
  .gloss-area {
    position: absolute;
    inset: 0;
    background:
      linear-gradient(125deg,
        var(--gloss-deep) 0%,
        rgba(11,11,12,0.85) 28%,
        rgba(29,29,30,0) 48%,
        rgba(29,29,30,0) 62%,
        rgba(60,60,62,0.6) 78%,
        var(--gloss-sheen) 100%);
  }
  .brand {
    position: absolute;
    right: 52px;
    top: 78px;
    width: 250px;
    text-align: center;
  }
  .brand__mark {
    display: block;
    width: 48px;
    height: 48px;
    margin: 0 auto 12px;
    border: 1.5px solid var(--ink);
  }
  .brand__name {
    font-weight: 300;
    font-size: 30px;
    letter-spacing: 1px;
    line-height: 1;
    text-transform: uppercase;
  }
  .brand__sub {
    margin-top: 8px;
    font-weight: 300;
    font-size: 14px;
    letter-spacing: 9px;
    text-transform: uppercase;
    padding-left: 9px;
  }

  /* back */
  .person {
    position: absolute;
    left: 70px;
    top: 130px;
    width: 140px;
    text-align: right;
  }
  .person__name {
    font-weight: 400;
    font-size: 15px;
    letter-spacing: 0.5px;
    text-transform: uppercase;
  }
  .person__role {
    margin-top: 3px;
    font-size: 9px;
    letter-spacing: 1px;
    color: var(--ink-soft);
    text-transform: uppercase;
  }
  .contact {
    position: absolute;
    left: 228px;
    top: 128px;
    list-style: none;
  }
  .contact__item {
    display: flex;
    align-items: center;
    gap: 7px;
    font-size: 15px;
    font-weight: 400;
    line-height: 23px;
  }
  .contact__icon { width: 12px; height: 12px; flex: none; }
</style>
</head>
<body>
  <section class="card card--front" aria-label="Business card front">
    <div class="gloss-area" role="img" aria-label="Large glossy studio monogram in spot varnish sweeping across the card"></div>
    <div class="brand">
      <span class="brand__mark" aria-hidden="true"></span>
      <div class="brand__name">Owen Tasker</div>
      <div class="brand__sub">Studios</div>
    </div>
  </section>

  <section class="card card--back" aria-label="Business card back">
    <div class="person">
      <div class="person__name">Owen Tasker</div>
      <div class="person__role">Photographer</div>
    </div>
    <ul class="contact">
      <li class="contact__item">
        <svg class="contact__icon" viewBox="0 0 12 12" aria-hidden="true">
          <rect x="0.5" y="0.5" width="11" height="11" rx="2.5" fill="none" stroke="#e9e9e9"/>
          <path d="M3.8 3.2 L5 4.6 L4.4 5.3 Q5.2 6.9 6.7 7.6 L7.4 7 L8.8 8.2 L8 9 Q5 8.6 3 4 Z" fill="#e9e9e9"/>
        </svg>
        <span>323-481-5206</span>
      </li>
      <li class="contact__item">
        <svg class="contact__icon" viewBox="0 0 12 12" aria-hidden="true">
          <rect x="0.5" y="0.5" width="11" height="11" rx="2.5" fill="none" stroke="#e9e9e9"/>
          <rect x="2.8" y="3.8" width="6.4" height="4.4" fill="none" stroke="#e9e9e9" stroke-width="0.9"/>
          <path d="M2.8 3.8 L6 6.3 L9.2 3.8" fill="none" stroke="#e9e9e9" stroke-width="0.9"/>
        </svg>
        <span>owentaskerlens@mailbox-example.net</span>
      </li>
      <li class="contact__item">
        <svg class="contact__icon" viewBox="0 0 12 12" aria-hidden="true">
          <rect x="0.5" y="0.5" width="11" height="11" rx="2.5" fill="none" stroke="#e9e9e9"/>
          <circle cx="6" cy="6" r="3" fill="none" stroke="#e9e9e9" stroke-width="0.9"/>
          <path d="M3 6 H9 M6 3 Q4.4 6 6 9 M6 3 Q7.6 6 6 9" fill="none" stroke="#e9e9e9" stroke-width="0.6"/>
        </svg>
        <span>taskerlens.examplefolio.net</span>
      </li>
    </ul>
  </section>
</body>
</html>
```